Concert festival poster

Poster invitation for 40th party designed to look like a concert festival. Using the samples attached as a guide, looking for a colorful, creative and eye catching invite.
The event will be held over a weekend at a farm, with music food, friends and drinks.

Target Market(s)

Party guests, friends and family

Industry/Entity Type

Festival

Colors

Designer to choose colors to be used in the design.

Requirements
Must have
• Brellafest- Mark Telford's 40th festival
• Event date- 5-7th October 2018. Main event 6th October 2018 from 3pm-late
• Come anytime over the weekend- food, drinks and fun provided.
• Address is 412 Stony Creek Lane, Marulan NSW
• All welcome, including children
• Bring your own tent or let us know and we can arrange glamping tent set-up on site
• RSVP by 1 May 2018 to Kate at kate.anne.telford@mailbox-demo.com or Mark at mtelford@vantor-telford.com.au
• Will add extra information on event at later stage- see below for editable section.
Nice to have
• Editable section to add details, preferable at bottom of poster.

```html
<!DOCTYPE html>
<html lang="en">
<head>
<meta charset="utf-8">
<title>Brellafest – Mark Telford's 40th Festival</title>
<link rel="stylesheet" href="https://fonts.googleapis.com/css2?family=Oswald:wght@700&family=Poiret+One&family=Open+Sans:wght@400&display=swap">
<style>
  :root {
    --card: #1e232d;
    --ink: #e6e6e6;
    --accent: #e2572c;
    --outline: #d9d9d9;
  }
  * { margin: 0; padding: 0; box-sizing: border-box; }
  html, body { width: 898px; height: 1200px; overflow: hidden; background: var(--card); }
  .poster { position: relative; width: 898px; height: 1200px; background: var(--card); font-family: "Open Sans", Arial, sans-serif; color: var(--ink); }
  .festival-name { position: absolute; left: 50px; top: 50px; width: 200px; height: 1090px; }
  .festival-name text { font-family: "Oswald", "Arial Narrow", sans-serif; font-weight: 700; }
  .divider-vertical { position: absolute; left: 285px; top: 60px; width: 2px; height: 1065px; background: var(--accent); }
  .host { position: absolute; left: 331px; top: 88px; font-size: 28px; letter-spacing: 0.3px; }
  .title { position: absolute; left: 326px; top: 150px; width: 545px; height: 125px; }
  .title text { font-family: "Poiret One", "Century Gothic", sans-serif; fill: var(--accent); }
  .rule { position: absolute; height: 2px; background: var(--accent); }
  .rule--main { left: 331px; top: 288px; width: 536px; }
  .rule--short { left: 376px; width: 417px; height: 1px; opacity: 0.9; }
  .info { position: absolute; left: 320px; width: 560px; text-align: center; font-size: 23px; line-height: 31px; }
  .info--small { font-size: 20px; line-height: 29px; }
  .tagline { position: absolute; left: 320px; width: 560px; top: 550px; text-align: center; font-family: "Poiret One", "Century Gothic", sans-serif; color: var(--accent); font-size: 32px; line-height: 46px; letter-spacing: -0.8px; }
</style>
</head>
<body>
<main class="poster">
  <svg class="festival-name" viewBox="0 0 200 1090" aria-label="Brellafest">
    <defs>
      <linearGradient id="festivalFill" x1="0" y1="1" x2="0" y2="0">
        <stop offset="0" stop-color="#e0473c"/>
        <stop offset="0.2" stop-color="#3f9d5a"/>
        <stop offset="0.38" stop-color="#e5742f"/>
        <stop offset="0.55" stop-color="#d9456d"/>
        <stop offset="0.72" stop-color="#3b9ec4"/>
        <stop offset="0.88" stop-color="#e35a2c"/>
        <stop offset="1" stop-color="#4aa85f"/>
      </linearGradient>
    </defs>
    <text transform="translate(185 1068) rotate(-90)" font-size="228" textLength="1050" lengthAdjust="spacingAndGlyphs" fill="url(#festivalFill)" stroke="var(--outline)" stroke-width="2">BRELLAFEST</text>
  </svg>

  <div class="divider-vertical"></div>

  <p class="host">Mark Telford's</p>
  <svg class="title" viewBox="0 0 545 125">
    <text x="2" y="108" font-size="118" textLength="540" lengthAdjust="spacingAndGlyphs">40th Festival</text>
  </svg>
  <div class="rule rule--main"></div>

  <p class="info" style="top:320px">5-7th October 2018.<br>Main event 6th October 2018 from 3pm-late</p>
  <p class="info" style="top:414px">Address: 412 Stony Creek Lane, Marulan NSW</p>
  <div class="rule rule--short" style="top:500px"></div>

  <p class="tagline">Come anytime over the weekend- food,<br>drinks and fun provided.</p>
  <p class="info" style="top:686px">All welcome, including children</p>
  <div class="rule rule--short" style="top:767px"></div>

  <p class="info" style="top:832px; line-height:28px">Bring your own tent or let us know<br>and we can<br>arrange glamping tent set-up on site</p>
  <div class="rule rule--short" style="top:958px"></div>

  <p class="info info--small" style="top:1015px">RSVP by 1 May 2018 to Kate at<br>kate.anne.telford@mailbox-demo.com<br>or Mark at mtelford@vantor-telford.com.au</p>
</main>
</body>
</html>
```